Casa Vero Inspections Business Card

I need a business card for my new company. The company is going to provide home inspections. The name of the company is Casa Vero Inspections. I am not sure if I want a single sided card or a double. I have a logo already that I want to incorporate into the card design. I was wondering if I should incorporate a catch phrase on my card or not. If I did the phrase would be "The Thorough Choice for Home Inspections" but i am unsure how or if to use it on a card. The following information needs to be on the card.
Home Inspection
My Name: Marcus T. Wolford Phone Number: 555-301-7762 Email: mwolford@casaveroinspections.com Website: www.casaveroinspections.com NY HI License # 27300519462

```html
<!DOCTYPE html>
<html lang="en">
<head>
<meta charset="utf-8">
<title>Casa Vero Inspections – Business Card</title>
<link href="https://fonts.googleapis.com/css2?family=Rubik:wght@400;500;700&display=swap" rel="stylesheet">
<style>
  :root {
    --backdrop: #d3d4d6;
    --card-light: #ffffff;
    --card-dark: #171717;
    --brand-blue: #0f6db3;
    --sky-blue: #6ec1f0;
    --white: #ffffff;
  }
  * { margin: 0; padding: 0; box-sizing: border-box; }
  html, body {
    width: 900px; height: 1200px; overflow: hidden;
    background: var(--backdrop);
    font-family: "Rubik", sans-serif;
  }
  .card {
    position: absolute; left: 133px;
    width: 633px; height: 364px;
  }
  .card--front { top: 210px; background: var(--card-light); }
  .card--back { top: 624px; background: var(--card-dark); color: var(--white); }

  .front-name {
    position: absolute; left: 0; right: 0; top: 188px;
    text-align: center; font-weight: 700; font-size: 36px;
    color: var(--brand-blue); letter-spacing: 0.5px;
  }
  .tagline {
    position: absolute; left: 0; right: 0; top: 314px;
    text-align: center; font-weight: 500; font-size: 15px;
    color: var(--brand-blue);
  }

  .back-name {
    position: absolute; left: 69px; width: 233px; top: 184px;
    text-align: center; font-weight: 700; font-size: 29px; line-height: 1.15;
    color: var(--white);
  }
  .divider {
    position: absolute; left: 317px; top: 115px;
    width: 1px; height: 137px; background: #cfcfcf;
  }
  .contact-person { position: absolute; left: 332px; top: 110px; }
  .person-name { font-weight: 500; font-size: 23px; color: var(--sky-blue); }
  .person-role { font-size: 15px; margin-top: 4px; }
  .contact-list {
    position: absolute; left: 332px; top: 190px; list-style: none;
    font-size: 14px;
  }
  .contact-list li { display: flex; align-items: center; height: 23.5px; }
  .contact-list svg { width: 15px; height: 15px; margin-right: 9px; flex: none; }
  .phone { letter-spacing: 3.5px; font-weight: 500; font-size: 15px; }
  .license {
    position: absolute; left: 0; right: 0; top: 316px;
    text-align: center; font-weight: 500; font-size: 14px; letter-spacing: 0.6px;
  }
</style>
</head>
<body>
  <section class="card card--front">
    <div class="front-name">Casa Vero Inspections</div>
    <p class="tagline">The Thorough Choice for Home Inspections</p>
  </section>

  <section class="card card--back">
    <div class="back-name">Casa Vero<br>Inspections</div>
    <div class="divider"></div>
    <div class="contact-person">
      <div class="person-name">Marcus T. Wolford</div>
      <div class="person-role">President</div>
    </div>
    <ul class="contact-list">
      <li>
        <svg viewBox="0 0 24 24" aria-hidden="true"><path fill="#6ec1f0" d="M6.6 10.8a15.1 15.1 0 0 0 6.6 6.6l2.2-2.2c.3-.3.7-.4 1-.2 1.1.4 2.3.6 3.6.6.6 0 1 .4 1 1V20c0 .6-.4 1-1 1A17 17 0 0 1 3 4c0-.6.4-1 1-1h3.5c.6 0 1 .4 1 1 0 1.3.2 2.5.6 3.6.1.3 0 .7-.2 1z"/></svg>
        <span class="phone">555-301-7762</span>
      </li>
      <li>
        <svg viewBox="0 0 24 24" aria-hidden="true"><rect x="2" y="5" width="20" height="14" fill="#6ec1f0"/><path d="M2 5l10 8 10-8" fill="none" stroke="#171717" stroke-width="2"/></svg>
        <span>mwolford@casaveroinspections.com</span>
      </li>
      <li>
        <svg viewBox="0 0 24 24" aria-hidden="true"><g fill="none" stroke="#6ec1f0" stroke-width="1.8"><circle cx="12" cy="12" r="9"/><ellipse cx="12" cy="12" rx="4" ry="9"/><path d="M3 12h18M5 7h14M5 17h14"/></g></svg>
        <span>www.casaveroinspections.com</span>
      </li>
    </ul>
    <p class="license">NY HI License # 27300519462</p>
  </section>
</body>
</html>
```